Business Card

We need some ideas for corporate business cards. I'm interested in a double sided card, with one side featuring our corporate logo, the other side with employee information.

Corporate colors, logo etc. available at www.brivalo.com

Industry/Entity Type

Business

Requirements
Must have
• The "Brivalo" logo with stylized "O"

Nice to have
• Preferred font is calibri

```html
<!DOCTYPE html>
<html lang="en">
<head>
<meta charset="utf-8">
<title>Brivalo Business Card</title>
<link rel="stylesheet" href="https://fonts.googleapis.com/css2?family=Carlito:wght@400;700&display=swap">
<style>
  :root {
    --page-bg: #ebeeec;
    --brand-blue: #315bc8;
    --title-blue: #4a6fd6;
    --card-dark: #0b0b0b;
    --text-light: #ffffff;
    --text-soft: #d3dcf6;
  }
  * { margin: 0; padding: 0; box-sizing: border-box; }
  html, body {
    width: 1011px; height: 1200px; overflow: hidden;
    background: var(--page-bg);
    font-family: "Carlito", "Calibri", sans-serif;
  }
  .canvas { position: relative; width: 1011px; height: 1200px; }
  .card { position: absolute; left: 120px; width: 767px; height: 444px; overflow: hidden; }

  /* Front: employee details */
  .card-front { top: 109px; background: var(--card-dark); }
  .card-front .pattern-area {
    position: absolute; left: 68px; top: 0; right: 0; bottom: 0;
    background: linear-gradient(135deg, #121212, #070707);
  }
  .side-band {
    position: absolute; left: 0; top: 0; width: 68px; height: 100%;
    background: var(--brand-blue);
  }
  .side-wordmark {
    position: absolute; left: 34px; top: 207px;
    transform: translate(-50%, -50%) rotate(-90deg);
    color: var(--text-light); font-weight: 700; font-size: 34px; letter-spacing: 3px;
    white-space: nowrap;
  }
  .employee-name {
    position: absolute; left: 68px; right: 0; top: 173px; text-align: center;
    color: var(--text-light); font-size: 39px; line-height: 48px;
  }
  .employee-title {
    position: absolute; left: 68px; right: 0; top: 220px; text-align: center;
    color: var(--title-blue); font-size: 30px; line-height: 36px;
  }
  .contact-lines {
    position: absolute; left: 77px; top: 350px;
    color: var(--text-soft); font-size: 21px; line-height: 30px;
  }
  .address-lines {
    position: absolute; right: 37px; top: 322px; text-align: right;
    color: var(--text-soft); font-size: 21px; line-height: 29.5px;
  }

  /* Back: corporate side */
  .card-back { top: 658px; background: var(--brand-blue); }
  .back-wordmark {
    position: absolute; left: 0; right: 0; top: 137px; text-align: center;
    color: var(--text-light); font-weight: 700; font-size: 78px; line-height: 95px; letter-spacing: 8px;
  }
  .pillar {
    position: absolute; top: 252px; width: 180px; margin-left: -90px;
    text-align: center; color: var(--text-light); font-size: 21px;
  }
  .pillar svg { display: block; margin: 10px auto 0; width: 54px; height: 54px; }
  .pillar-technology { left: 142px; }
  .pillar-solutions { left: 391px; }
  .pillar-vision { left: 644px; }
</style>
</head>
<body>
<main class="canvas">
  <section class="card card-front" aria-label="Business card front">
    <div class="pattern-area" role="img" aria-label="Subtle dark repeating pattern of the company web address"></div>
    <div class="side-band"><span class="side-wordmark">BRIVALO</span></div>
    <p class="employee-name">John Doe</p>
    <p class="employee-title">Senior Software Engineer</p>
    <div class="contact-lines">
      <p>Tel:&nbsp; +1 555 210 4830</p>
      <p>Fax: +1 555 210 4831</p>
    </div>
    <div class="address-lines">
      <p>742 Harbor Point Lane</p>
      <p>Suite 540</p>
      <p>Fairview, 43015, OH</p>
    </div>
  </section>

  <section class="card card-back" aria-label="Business card back">
    <p class="back-wordmark">BRIVALO</p>
    <div class="pillar pillar-technology">
      <span>Technology</span>
      <svg viewBox="0 0 54 54" aria-hidden="true">
        <g fill="#fff" transform="translate(27 27)">
          <rect x="-4.5" y="-22" width="9" height="44" rx="2"/>
          <rect x="-4.5" y="-22" width="9" height="44" rx="2" transform="rotate(45)"/>
          <rect x="-4.5" y="-22" width="9" height="44" rx="2" transform="rotate(90)"/>
          <rect x="-4.5" y="-22" width="9" height="44" rx="2" transform="rotate(135)"/>
          <circle r="16"/>
        </g>
        <circle cx="27" cy="27" r="6.5" fill="var(--brand-blue)"/>
      </svg>
    </div>
    <div class="pillar pillar-solutions">
      <span>Solutions</span>
      <svg viewBox="0 0 54 54" aria-hidden="true">
        <circle cx="27" cy="27" r="23" fill="#fff"/>
        <circle cx="27" cy="27" r="17" fill="var(--brand-blue)"/>
        <path d="M36 18 L30 30 L18 36 L24 24 Z" fill="#fff"/>
        <circle cx="27" cy="27" r="2.5" fill="var(--brand-blue)"/>
      </svg>
    </div>
    <div class="pillar pillar-vision">
      <span>Vision</span>
      <svg viewBox="0 0 70 54" aria-hidden="true" style="width:70px">
        <path d="M2 27 C14 9 56 9 68 27 C56 45 14 45 2 27 Z" fill="#fff"/>
        <circle cx="35" cy="27" r="11" fill="var(--brand-blue)"/>
        <circle cx="35" cy="27" r="5" fill="#fff"/>
      </svg>
    </div>
  </section>
</main>
</body>
</html>
```